Bright Canyon, LLC Business Card Design

We need a product business card designed for a new company Bright Canyon, LLC. We make and resell waterless RV cleaner, polish and protectant. It cleans and protects in a simple spray and wipe step leaving the surface protected and conditioned to repel dust, dirt, water, smudges, bugs and fingerprints while preventing fogging. Safe on acrylic, clarisheet, durvane, plastic, rubber, painted surfaces, chrome, stainless, aluminum, vinyl, leather, glass.... This is an eco-friendly green product.

We want to play off the company name to tell the consumer that the product is easy to use and associate to the nostalgics 1950's in the USA... Thinking old travel trailer with hot rod truck pulling it as the graphic, maybe the husband cleaning the truck and the wife cleaning the trailer for a Bright Canyon surface.
Updates

Just posted our newly finished logo. Need to have "Cleaner and Protectant" added to the design as well. Thanks everyone that has submitted thus far, i am working to get comments on all.

If you need a different file format, please let me know. Thank you.

Most important info, is the logo, website and the words "Cleaner" or "Clean" along "Protectant" or "Protect" the remainder is of less importance. Highlight: www.brightcanyoncleaner.example Focus is on company brand for Brighter Canyon Cleaner product: However, need a section for the following contact info: John Doe (xxx) xxx-xxxx email address Would like space for QR Code if possible.

Target Market(s)

Adults in the USA between ages of 35-75 that are actively involved in the Recreational Vehicle (RV), travel trailer, and hot rod lifestyle. We are targeting the RV marked of the high end travel, 5th wheel and bus RV market. Along with hot rods, automotive and motorcycle market.

Industry/Entity Type

Travel

Requirements
Must have
• Most important info, is the logo, website and the words "Cleaner" or "Clean" along "Protectant" or "Protect" the remainder is of less importance.

Highlight:
www.brightcanyoncleaner.example

Focus is on company brand for Brighter Canyon Cleaner product: However, need a section for the following contact info:

John Doe
(xxx) xxx-xxxx
email address
Nice to have
• Would like a space for a QR Code.

```html
<!DOCTYPE html>
<html lang="en">
<head>
<meta charset="utf-8">
<title>Bright Canyon – Business Card</title>
<link href="https://fonts.googleapis.com/css2?family=Open+Sans:wght@400;600;800&display=swap" rel="stylesheet">
<style>
  :root {
    --backdrop: #a9a9a9;
    --card: #ffffff;
    --ink: #3c3a3b;
    --ink-soft: #4a4a4a;
    --accent: #f05a35;
    --edge: #6b6b6b;
    --qr-line: #9a9a9a;
  }
  * { margin: 0; padding: 0; box-sizing: border-box; }
  html, body {
    width: 1200px; height: 894px; overflow: hidden;
    background: var(--backdrop);
    font-family: "Open Sans", Arial, sans-serif;
  }
  .sheet { position: relative; width: 1200px; height: 894px; }
  .card {
    position: absolute; left: 250px; width: 700px; height: 400px;
    background: var(--card);
    box-shadow: 0 6px 18px rgba(0,0,0,.25);
    overflow: hidden;
  }
  .card--front { top: 30px; }
  .card--back { top: 464px; }
  .card__bands { position: absolute; inset: 0; }

  .brand {
    position: absolute;
    display: flex; flex-direction: column; align-items: flex-start; gap: 6px;
  }
  .card--front .brand { left: 50%; top: 50%; transform: translate(-50%, -50%); }
  .card--back .brand { left: 380px; top: 140px; }

  .wordmark {
    display: flex; align-items: center; gap: 12px;
    font-weight: 800; font-size: 46px; letter-spacing: -1px; line-height: 1.1;
    color: var(--ink); text-transform: uppercase; white-space: nowrap;
  }
  .card--back .wordmark { font-size: 34px; gap: 10px; }
  .wordmark__dot { width: 18px; height: 18px; background: var(--accent); flex: none; }
  .card--back .wordmark__dot { width: 14px; height: 14px; }

  .tagline {
    padding-left: 30px;
    font-weight: 600; font-size: 18px; letter-spacing: 3px;
    color: var(--accent); text-transform: uppercase; white-space: nowrap;
  }
  .card--back .tagline { padding-left: 24px; font-size: 13px; letter-spacing: 2px; }

  .contact { position: absolute; left: 60px; top: 60px; color: var(--ink-soft); }
  .contact__name { font-weight: 800; font-size: 24px; color: var(--ink); letter-spacing: .5px; }
  .contact__role { font-size: 20px; font-weight: 400; margin-bottom: 26px; }
  .contact__list { list-style: none; width: 290px; }
  .contact__item {
    display: flex; justify-content: flex-end; align-items: center; gap: 10px;
    font-size: 15px; line-height: 26px; white-space: nowrap;
  }
  .contact__item--plain { padding-right: 26px; }
  .contact__item--web { font-weight: 600; color: var(--ink); }
  .contact__bullet {
    width: 16px; height: 16px; border-radius: 50%; background: var(--ink); flex: none;
  }

  .qr-space {
    position: absolute; left: 540px; top: 250px;
    width: 100px; height: 100px;
    border: 2px dashed var(--qr-line);
  }
</style>
</head>
<body>
<main class="sheet">

  <section class="card card--front" aria-label="Card front">
    <svg class="card__bands" viewBox="0 0 700 400" aria-hidden="true">
      <polygon points="0,0 140,0 110,20 0,20" fill="var(--accent)"/>
      <polygon points="0,20 22,40 22,260 0,280" fill="var(--edge)"/>
      <polygon points="700,400 560,400 590,380 700,380" fill="var(--accent)"/>
      <polygon points="700,380 678,360 678,120 700,100" fill="var(--edge)"/>
    </svg>
    <div class="brand">
      <div class="wordmark"><span class="wordmark__dot"></span>Bright Canyon</div>
      <p class="tagline">Cleaner and Protectant</p>
    </div>
  </section>

  <section class="card card--back" aria-label="Card back">
    <svg class="card__bands" viewBox="0 0 700 400" aria-hidden="true">
      <polygon points="420,0 700,0 700,18 440,18" fill="var(--accent)"/>
      <polygon points="0,0 22,20 22,150 0,170" fill="var(--edge)"/>
      <polygon points="0,400 180,400 160,380 0,380" fill="var(--accent)"/>
      <polygon points="0,380 22,360 22,240 0,220" fill="var(--edge)"/>
      <polygon points="700,380 678,360 678,200 700,180" fill="var(--edge)"/>
    </svg>

    <div class="contact">
      <p class="contact__name">MARK DELANEY</p>
      <p class="contact__role">GENERAL MANAGER</p>
      <ul class="contact__list">
        <li class="contact__item contact__item--plain">Delaney St, 456D</li>
        <li class="contact__item contact__item--plain">Lorem City, Ashford</li>
        <li class="contact__item">001 555 210 487<span class="contact__bullet"></span></li>
        <li class="contact__item">001 555 210 487<span class="contact__bullet"></span></li>
        <li class="contact__item">info@brightcanyon.example<span class="contact__bullet"></span></li>
        <li class="contact__item contact__item--web">www.brightcanyoncleaner.example<span class="contact__bullet"></span></li>
      </ul>
    </div>

    <div class="brand">
      <div class="wordmark"><span class="wordmark__dot"></span>Bright Canyon</div>
      <p class="tagline">Cleaner and Protectant</p>
    </div>

    <div class="qr-space" role="img" aria-label="Space reserved for QR code"></div>
  </section>

</main>
</body>
</html>
```